Square Business Cards for Our Restaurant / Event Venue

We need square business cards designed for the management team of our event venue and restaurant. On one side of the card should be the the Harbor Lantern 7 logo and URL www.harborlantern7.example. On the other side should be the Ember Logo and URL www.emberhall7.example. All employee details should be on the side with Ember logo. There will be a total of 5 cards to be created with the design.

Clara Bennquist
clara@harborlantern7.example

main 555.418.3072
direct 555.730.2946

4831 West Orchard Lane SE
Washington, DC 90417

Industry/Entity Type

Business

```html
<!DOCTYPE html>
<html lang="en">
<head>
<meta charset="utf-8">
<title>Harbor Lantern 7 – Square Business Cards</title>
<link rel="stylesheet" href="https://fonts.googleapis.com/css2?family=Questrial&family=Lato:wght@400&display=swap">
<style>
  :root {
    --backdrop: #e9e6e2;
    --card: #161616;
    --ink-light: #ffffff;
    --ink-soft: #f1f1f1;
    --ink-muted: #bdbdbd;
    --accent: #c1272d;
    --seal: #b72025;
    --seal-ink: #111111;
  }
  * { box-sizing: border-box; margin: 0; padding: 0; }
  html, body {
    width: 1200px; height: 960px; overflow: hidden;
    background: var(--backdrop);
  }
  .canvas { position: relative; width: 1200px; height: 960px; }
  .card {
    position: absolute; top: 240px; width: 484px; height: 484px;
    background: var(--card);
    box-shadow: 0 6px 14px rgba(0,0,0,0.25);
  }
  .card--front { left: 128px; }
  .card--back { left: 653px; }

  .wordmark {
    position: absolute; left: 0; right: 0; top: 62px;
    text-align: center;
    font-family: "Questrial", sans-serif;
    font-size: 68px; color: var(--ink-light);
    letter-spacing: 1px;
  }
  .person-name {
    position: absolute; left: 0; right: 0; top: 224px;
    text-align: center;
    font-family: "Questrial", sans-serif;
    font-weight: 400;
    font-size: 33px; color: var(--ink-light);
  }
  .contact {
    position: absolute;
    font-family: "Lato", sans-serif;
    font-size: 20px; color: var(--ink-soft);
    display: flex; align-items: center; gap: 8px;
    white-space: nowrap;
  }
  .contact svg { flex: none; }
  .contact--email { left: 52px; top: 288px; }
  .contact--main { left: 52px; top: 327px; }
  .contact--direct { right: 26px; top: 327px; }
  .divider {
    position: absolute; left: 26px; top: 366px;
    width: 430px; height: 3px; background: var(--accent);
  }
  .address {
    position: absolute; left: 0; right: 0; top: 379px;
    font-family: "Lato", sans-serif; font-style: normal;
    font-size: 20px; line-height: 34px; color: var(--ink-soft);
    text-align: center;
  }
  .address .pin { vertical-align: -3px; margin-right: 4px; }
  .site-url {
    position: absolute; left: 0; right: 0;
    text-align: center;
    font-family: "Lato", sans-serif;
    font-size: 14px; letter-spacing: 0.5px;
    color: var(--ink-muted);
  }
  .card--front .site-url { top: 454px; }
  .card--back .site-url { top: 420px; font-size: 16px; }

  .seal {
    position: absolute; left: 107px; top: 107px;
    width: 272px; height: 272px; border-radius: 50%;
    background: var(--seal);
    display: flex; align-items: center; justify-content: center;
    text-align: center;
  }
  .seal-name {
    font-family: "Questrial", sans-serif;
    font-size: 38px; line-height: 44px; color: var(--seal-ink);
  }
</style>
</head>
<body>
<main class="canvas">
  <section class="card card--front">
    <div class="wordmark">Ember</div>
    <h1 class="person-name">Clara Bennquist</h1>

    <p class="contact contact--email">
      <svg width="24" height="16" viewBox="0 0 24 16" aria-hidden="true">
        <rect x="0" y="0" width="24" height="16" fill="var(--accent)"/>
        <path d="M1 1 L12 9 L23 1" fill="none" stroke="var(--card)" stroke-width="1.6"/>
        <path d="M1 15 L9 7 M23 15 L15 7" fill="none" stroke="var(--card)" stroke-width="1.2"/>
      </svg>
      clara@harborlantern7.example
    </p>

    <p class="contact contact--main">
      <svg width="26" height="18" viewBox="0 0 26 18" aria-hidden="true">
        <path d="M1 6 Q13 -2 25 6 L22 9 L18 7 L18 5 Q13 3 8 5 L8 7 L4 9 Z" fill="var(--accent)"/>
        <path d="M5 10 L9 7 L17 7 L21 10 L21 18 L5 18 Z" fill="var(--accent)"/>
        <circle cx="13" cy="13" r="2.4" fill="var(--card)"/>
      </svg>
      555.418.3072
    </p>

    <p class="contact contact--direct">
      555.730.2946
      <svg width="14" height="22" viewBox="0 0 14 22" aria-hidden="true">
        <rect x="1" y="1" width="12" height="20" rx="2" fill="none" stroke="var(--accent)" stroke-width="2"/>
        <rect x="3" y="4" width="8" height="11" fill="var(--accent)"/>
        <circle cx="7" cy="18" r="1.2" fill="var(--accent)"/>
      </svg>
    </p>

    <div class="divider"></div>

    <address class="address">
      <svg class="pin" width="16" height="22" viewBox="0 0 16 22" aria-hidden="true">
        <path d="M8 0 C3.6 0 0 3.5 0 7.8 C0 13.5 8 22 8 22 C8 22 16 13.5 16 7.8 C16 3.5 12.4 0 8 0 Z" fill="var(--accent)"/>
        <circle cx="8" cy="8" r="3" fill="var(--card)"/>
      </svg>4831 West Orchard Lane SE<br>
      Washington, DC 90417
    </address>

    <p class="site-url">www.emberhall7.example</p>
  </section>

  <section class="card card--back">
    <div class="seal">
      <div class="seal-name">Harbor<br>Lantern 7</div>
    </div>
    <p class="site-url">www.harborlantern7.example</p>
  </section>
</main>
</body>
</html>
```